Landingpage design for Movarabroker website

We need a design for a responsive 1 page landing page.
Good example: https://www.kelvaro.com/
On the homepage we will like to have a explanation video
attached you can find the logo's

About the website Movara.offers:
Movara.offers is a “Broker” we bring buyers and sellers together and facilitate transactions

Simple
quickly
Actuel
Compare (who is the best provider, at what price)
great offer
independent
1 invoice

Target Market(s)

BtoB

Number of Pages Required

1 page

Requirements
Must have
• On the homepage we will like to have a explanation video
Nice to have
• something between shipper and carrier and bring them togheter
• We will focus us first on fish transport... maybe you can add something
• Map from europe that shows our workarea

```html
<!DOCTYPE html>
<html lang="en">
<head>
<meta charset="utf-8">
<title>Movara Offers – Landing Page Desktop &amp; Mobile</title>
<link href="https://fonts.googleapis.com/css2?family=Poppins:wght@300;400;500;600&display=swap" rel="stylesheet">
<style>
:root{
  --blue:#2eaad5;
  --blue-dark:#2496bf;
  --paper:#f4f4f4;
  --grey:#e4e4e4;
  --ink:#222;
  --black:#000;
  --slate:#4a4a4a;
  --white:#fff;
}
*{box-sizing:border-box;margin:0;padding:0}
html,body{width:1200px;height:1200px;overflow:hidden;background:var(--white);font-family:'Poppins',sans-serif;color:var(--ink)}
.board{position:relative;width:1200px;height:1200px}
.board-title{position:absolute;left:710px;top:28px;font-size:10px;font-weight:500;text-decoration:underline}
.frame{position:absolute;overflow:hidden}
.desktop{left:0;top:0;width:670px;height:1198px}
.mobile{left:713px;top:110px;width:462px;height:924px}
.block{position:absolute;left:0;width:100%}
.fill{position:absolute}
.brand{display:flex;align-items:center;gap:6px;color:var(--white);font-weight:600;letter-spacing:.5px;line-height:1}
.brand-dot{width:14px;height:14px;border-radius:50%;background:var(--white)}
.topbar{background:var(--blue);display:flex;align-items:center}
.nav{display:flex;gap:16px;color:var(--white);font-size:9px;font-weight:500}
.burger{display:flex;flex-direction:column;gap:3px}
.burger span{display:block;width:18px;height:2px;background:var(--white)}
h1,h2{font-weight:500;color:var(--blue);line-height:1.05}
.text{font-weight:300;line-height:1.3}
.link{font-weight:600;text-decoration:underline;display:inline-flex;gap:6px;align-items:center}
.link::after{content:"›";text-decoration:none;font-weight:600}
.btn{display:inline-block;background:var(--blue);color:var(--white);font-size:10px;font-weight:500;text-align:center}
.play{position:absolute;border-radius:50%;background:var(--white);display:flex;align-items:center;justify-content:center}
.play::after{content:"";border-left:5px solid var(--ink);border-top:3px solid transparent;border-bottom:3px solid transparent}
.photo-road{background:linear-gradient(180deg,#6d7f95 0%,#3e5068 55%,#2b3440 100%)}
.photo-mountain{background:linear-gradient(180deg,#c8d0d8 0%,#6f7f78 40%,#2f4a2e 75%,#3c3f3f 100%)}
.photo-fish{background:linear-gradient(135deg,#4a4f54 0%,#262a2e 60%,#1a1c1e 100%)}
.photo-map{background:linear-gradient(110deg,#a6cdf8 0%,#a6cdf8 45%,#ecece6 60%,#c9e6a9 100%)}
.icons{display:flex;gap:12px;align-items:center;justify-content:center}
.dot{border-radius:50%;background:currentColor}
.footer{background:var(--blue);color:var(--white)}
</style>
</head>
<body>
<main class="board">
  <p class="board-title">Movara Offers Website Design - Desktop &amp; Mobile Versions.</p>

  <!-- Desktop -->
  <section class="frame desktop">
    <header class="block topbar" style="top:0;height:44px;padding:0 14px 0 16px">
      <div class="brand" style="font-size:9px"><span class="brand-dot"></span>MOVARA<br>OFFERS</div>
      <nav class="nav" style="margin-left:26px"><span>About us</span><span>Pricing</span><span>FAQ</span><span>Contact</span></nav>
      <nav class="nav" style="margin-left:auto;gap:13px;align-items:center"><span>Log in</span><span>Register</span>
        <svg width="14" height="14" viewBox="0 0 14 14"><circle cx="6" cy="6" r="4.5" fill="none" stroke="#fff" stroke-width="1.8"/><line x1="9.3" y1="9.3" x2="13" y2="13" stroke="#fff" stroke-width="2"/></svg>
        <div class="burger"><span></span><span></span><span></span></div></nav>
    </header>

    <div class="block" style="top:44px;height:257px;background:var(--paper)">
      <h1 style="position:absolute;left:26px;top:41px;font-size:23px">Looking for a transport<br>company?</h1>
      <p class="text" style="position:absolute;left:26px;top:107px;font-size:11px">We bring you together and find the best<br>and most efficient way for your shipments</p>
      <p class="text" style="position:absolute;left:26px;top:150px;font-size:11px">Movara.offers is <b style="font-weight:600">FREE</b></p>
      <span class="btn" style="position:absolute;left:26px;top:188px;width:81px;height:24px;line-height:24px">Register</span>
      <span class="btn" style="position:absolute;left:115px;top:188px;width:82px;height:24px;line-height:24px">Login</span>
      <div class="fill photo-road" role="img" aria-label="Explanation video: truck on a coastal road" style="left:356px;top:45px;width:287px;height:174px"></div>
      <span class="play" style="left:474px;top:107px;width:50px;height:50px"></span>
    </div>

    <div class="block" style="top:301px;height:177px;background:var(--grey)">
      <div class="fill photo-mountain" role="img" aria-label="Truck driving through snowy mountains" style="left:0;top:0;width:335px;height:177px"></div>
      <h2 style="position:absolute;left:356px;top:22px;font-size:16px">Why should I use Movara.offers?</h2>
      <p class="text" style="position:absolute;left:356px;top:54px;width:280px;font-size:10px">Movara.offers is a “Broker” we bring buyers and sellers together and facilitate transactions. Adipisci tractatos vis cu, elit omnium mel ut, brute diceret et pro. An primis nominavi mei, ei vel brute scaevola accusata.</p>
      <span class="link" style="position:absolute;left:356px;top:137px;font-size:10px">How It Works for Customers</span>
    </div>

    <div class="block photo-fish" role="img" aria-label="Fresh fish in a crate" style="top:478px;height:195px">
      <h2 style="position:absolute;left:22px;top:27px;font-size:16px;color:var(--white)">Transport Solutions</h2>
      <p class="text" style="position:absolute;left:22px;top:61px;width:260px;font-size:10px;color:var(--white)">Adipisci tractatosvis cu, elit omnium mel ut, brute diceret et pro. An primis nominavi mei, ei vel brute scaevola accusata. elit omnium mel ut, brute diceret et pro. An primis nominavi mei, ei vel evola accusata.</p>
      <span class="link" style="position:absolute;left:22px;top:144px;font-size:10.5px;color:var(--white)">Organise your transport</span>
    </div>

    <div class="block" style="top:673px;height:236px;background:var(--grey)">
      <h2 style="position:absolute;left:26px;top:46px;font-size:16px">Destination Europe</h2>
      <p class="text" style="position:absolute;left:26px;top:78px;width:260px;font-size:10px">Adipisci tractatosvis cu, elit omnium mel ut, brute diceret et pro. An primis nominavi mei, ei vel brute scaevola accusata. elit omnium mel ut, brute diceret et pro. An primis nominavi mei, ei vel evola accusata.</p>
      <span class="link" style="position:absolute;left:26px;top:163px;font-size:10px">How It Works for Customers</span>
      <div class="fill photo-map" role="img" aria-label="Map of the work area" style="left:331px;top:0;width:339px;height:236px"></div>
    </div>

    <div class="block" style="top:909px;height:132px">
      <div class="fill" style="left:0;top:0;width:330px;height:132px;background:var(--black);color:var(--white);text-align:center">
        <p style="margin-top:38px;font-size:20px;font-weight:500;letter-spacing:1px">Movara.offers is Free?</p>
        <p class="text" style="margin-top:6px;font-size:10.5px">Click Here to find out more about our promotion ›</p>
      </div>
      <div class="fill" style="left:330px;top:0;width:340px;height:132px;background:var(--slate);color:var(--white);text-align:center">
        <p style="margin-top:38px;font-size:20px;font-weight:400;letter-spacing:1.5px">Contact Us</p>
        <div class="icons" style="margin-top:12px">
          <span class="dot" style="width:12px;height:12px"></span><span class="dot" style="width:12px;height:12px"></span>
          <svg width="18" height="12" viewBox="0 0 18 12"><rect x=".5" y=".5" width="17" height="11" fill="#fff"/><path d="M.5 .5 9 7l8.5-6.5" fill="none" stroke="#4a4a4a" stroke-width="1.2"/></svg>
          <span class="dot" style="width:12px;height:12px"></span>
        </div>
      </div>
    </div>

    <footer class="block footer" style="top:1041px;height:157px">
      <div class="brand" style="position:absolute;left:30px;top:38px;font-size:12px"><span class="brand-dot" style="width:22px;height:22px"></span>MOVARA<br>OFFERS</div>
      <p class="text" style="position:absolute;left:24px;top:82px;font-size:9.5px">We bring you together and find the best<br>and most efficient way for your shipments</p>
      <p style="position:absolute;left:24px;top:122px;font-size:10px;font-weight:500">Copyright 2017 Movara.offers, All rights reserved</p>
      <ul style="position:absolute;left:330px;top:36px;list-style:none;font-size:11px;font-weight:500;line-height:17.5px"><li>About us</li><li>Pricing</li><li>FAQ</li><li>Contact Us</li></ul>
      <p style="position:absolute;left:467px;top:36px;font-size:11px;font-weight:500;text-decoration:underline">Follow Us</p>
      <div class="icons" style="position:absolute;left:467px;top:62px">
        <span class="dot" style="width:10px;height:10px"></span><span class="dot" style="width:10px;height:10px"></span>
        <svg width="15" height="10" viewBox="0 0 15 10"><rect x=".5" y=".5" width="14" height="9" fill="#fff"/><path d="M.5 .5 7.5 6l7-5.5" fill="none" stroke="#2eaad5" stroke-width="1"/></svg>
        <span class="dot" style="width:10px;height:10px"></span>
      </div>
    </footer>
  </section>

  <!-- Mobile -->
  <section class="frame mobile">
    <header class="block topbar" style="top:0;height:48px;padding:0 14px 0 16px">
      <div class="brand" style="font-size:8px"><span class="brand-dot"></span>MOVARA<br>OFFERS</div>
      <div style="margin-left:auto;display:flex;gap:14px;align-items:center">
        <svg width="16" height="16" viewBox="0 0 14 14"><circle cx="6" cy="6" r="4.5" fill="none" stroke="#fff" stroke-width="1.8"/><line x1="9.3" y1="9.3" x2="13" y2="13" stroke="#fff" stroke-width="2"/></svg>
        <div class="burger" style="gap:4px"><span style="width:22px"></span><span style="width:22px"></span><span style="width:22px"></span></div>
      </div>
    </header>

    <div class="block" style="top:48px;height:255px;background:var(--paper);text-align:center">
      <h1 style="margin-top:20px;font-size:19px">Looking for a transport<br>company?</h1>
      <p class="text" style="margin-top:7px;font-size:9px;line-height:1.1">We bring you together and find the best<br>and most efficient way for your shipments</p>
      <p class="text" style="margin-top:10px;font-size:9px">Movara.offers is <b style="font-weight:600">FREE</b></p>
      <div class="fill photo-road" role="img" aria-label="Explanation video: truck on a coastal road" style="left:123px;top:111px;width:214px;height:130px"></div>
      <span class="play" style="left:211px;top:157px;width:37px;height:37px"></span>
    </div>

    <div class="block" style="top:303px;height:125px;background:var(--grey)">
      <div class="fill photo-mountain" role="img" aria-label="Truck driving through snowy mountains" style="left:0;top:0;width:229px;height:125px"></div>
      <h2 style="position:absolute;left:243px;top:14px;font-size:11.5px">Why should I use Movara.offers?</h2>
      <p class="text" style="position:absolute;left:243px;top:38px;width:205px;font-size:7px;line-height:1.3">Movara.offers is a “Broker” we bring buyers and sellers together and facilitate transactions. Adipisci tractatos vis cu, elit omnium mel ut, brute diceret et pro. An primis nominavi mei, ei vel brute scaevola accusata.</p>
      <span class="link" style="position:absolute;left:243px;top:97px;font-size:7.5px">How It Works for Customers</span>
    </div>

    <div class="block photo-fish" role="img" aria-label="Fresh fish in a crate" style="top:428px;height:152px">
      <h2 style="position:absolute;left:17px;top:20px;font-size:12.5px;color:var(--white)">Transport Solutions</h2>
      <p class="text" style="position:absolute;left:17px;top:46px;width:205px;font-size:7.5px;color:var(--white)">Adipisci tractatosvis cu, elit omnium mel ut, brute diceret et pro. An primis nominavi mei, ei vel brute scaevola accusata. elit omnium mel ut, brute diceret et pro. An primis nominavi mei, ei vel evola accusata.</p>
      <span class="link" style="position:absolute;left:17px;top:111px;font-size:8px;color:var(--white)">Organise your transport</span>
    </div>

    <div class="block" style="top:580px;height:168px;background:var(--grey)">
      <h2 style="position:absolute;left:14px;top:32px;font-size:12px">Destination Europe</h2>
      <p class="text" style="position:absolute;left:14px;top:56px;width:195px;font-size:7px">Adipisci tractatosvis cu, elit omnium mel ut, brute diceret et pro. An primis nominavi mei, ei vel brute scaevola accusata. elit omnium mel ut, brute diceret et pro. An primis nominavi mei, ei vel evola accusata.</p>
      <span class="link" style="position:absolute;left:14px;top:114px;font-size:7.5px">How It Works for Customers</span>
      <div class="fill photo-map" role="img" aria-label="Map of the work area" style="left:229px;top:0;width:233px;height:168px"></div>
    </div>

    <div class="block" style="top:748px;height:92px">
      <div class="fill" style="left:0;top:0;width:229px;height:92px;background:var(--black);color:var(--white);text-align:center">
        <p style="margin-top:26px;font-size:14px;font-weight:500;letter-spacing:1px">Movara.offers is Free?</p>
        <p class="text" style="margin-top:3px;font-size:6.5px;text-decoration:underline">Click Here to find out more about our promotion</p>
      </div>
      <div class="fill" style="left:229px;top:0;width:233px;height:92px;background:var(--slate);color:var(--white);text-align:center">
        <p style="margin-top:26px;font-size:14px;letter-spacing:1.2px">Contact Us</p>
        <div class="icons" style="margin-top:7px;gap:10px">
          <span class="dot" style="width:9px;height:9px"></span><span class="dot" style="width:9px;height:9px"></span>
          <svg width="13" height="9" viewBox="0 0 15 10"><rect x=".5" y=".5" width="14" height="9" fill="#fff"/><path d="M.5 .5 7.5 6l7-5.5" fill="none" stroke="#4a4a4a" stroke-width="1"/></svg>
          <span class="dot" style="width:9px;height:9px"></span>
        </div>
      </div>
    </div>

    <footer class="block footer" style="top:840px;height:84px">
      <div class="brand" style="position:absolute;left:14px;top:10px;font-size:6px"><span class="brand-dot" style="width:12px;height:12px"></span>MOVARA<br>OFFERS</div>
      <p class="text" style="position:absolute;left:14px;top:38px;font-size:6.5px;line-height:1.2">We bring you together and find the best<br>and most efficient way for your shipments</p>
      <ul style="position:absolute;left:257px;top:10px;list-style:none;font-size:7px;font-weight:500;line-height:11.5px"><li>About us</li><li>Pricing</li><li>FAQ</li><li>Contact Us</li></ul>
      <p style="position:absolute;left:350px;top:10px;font-size:7.5px;font-weight:500;text-decoration:underline">Follow Us</p>
      <div class="icons" style="position:absolute;left:350px;top:30px;gap:9px">
        <span class="dot" style="width:7px;height:7px"></span><span class="dot" style="width:7px;height:7px"></span>
        <svg width="11" height="7" viewBox="0 0 15 10"><rect x=".5" y=".5" width="14" height="9" fill="#fff"/><path d="M.5 .5 7.5 6l7-5.5" fill="none" stroke="#2eaad5" stroke-width="1"/></svg>
        <span class="dot" style="width:7px;height:7px"></span>
      </div>
      <p style="position:absolute;left:0;width:100%;top:68px;text-align:center;font-size:7px;font-weight:500">Copyright 2017 Movara.offers, All rights reserved</p>
    </footer>
  </section>
</main>
</body>
</html>
```